Hot-air ballooning company needs a DL-size flyer

Skylark Aerial Tours is a hot-air ballooning company which flies passengers in the King Valley, Victoria, Australia.
We need a 2-sided DL-size flyer which promotes our hot-air balloon flights and packages.
Most of our customers are couples, and we want the flyer design to communicate safety, adventure, and romance.
The flyer should make the best use of our images which we provide, and we've also included a document with the text for the flyer.
Updates

2 days is not long enough to gather designs, the brief never asked me what my deadline should be.

Target Market(s)

Couples, buyers are majority female, between the ages of 20-60

Industry/Entity Type

Tourism

Font styles to use
Sans Serif

Colors

Designer to choose colors to be used in the design.

Requirements
Must have
• Communicate safety, adventure, and romance
• Use images
Nice to have
• There is a lot of text, it would be great if you could make it look like as little text as possible
Should not have
• No childish designs

```html
<!DOCTYPE html>
<html lang="en">
<head>
<meta charset="utf-8">
<title>King Valley Hot-Air Ballooning – DL Flyer</title>
<link rel="stylesheet" href="https://fonts.googleapis.com/css2?family=Oswald:wght@600;700&family=Open+Sans:ital,wdth,wght@0,75..100,400..800;1,75..100,400..800&display=swap">
<style>
  :root{
    --red:#e30613;
    --red-dark:#b3040f;
    --black:#141414;
    --ink:#1c1c1c;
    --white:#ffffff;
    --stage:#333333;
    --sky-orange:#f29a3a;
    --rule:#bbbbbb;
  }
  *{box-sizing:border-box;margin:0;padding:0}
  html,body{width:900px;height:1200px;overflow:hidden}
  body{background:var(--stage);position:relative;font-family:"Open Sans",Arial,sans-serif;color:var(--ink)}
  .panel{position:absolute;background:var(--white);overflow:hidden}
  .panel--front{left:62px;top:182px;width:384px;height:770px}
  .panel--back{left:488px;top:190px;width:374px;height:750px}
  .panel svg.art{position:absolute;left:0;top:0}
  .title{position:absolute;right:22px;top:34px;text-align:right;color:var(--white);font-family:"Oswald",Impact,sans-serif;font-weight:700;line-height:.95}
  .title__main{display:block;font-size:64px;letter-spacing:1px}
  .title__sub{display:block;font-size:46px}
  .title__tag{display:block;font-size:13px;font-weight:600;margin-top:6px;letter-spacing:.3px}
  .headline{position:absolute;left:22px;top:478px;white-space:nowrap;font-weight:800;font-style:italic;font-stretch:78%;font-size:17px;line-height:20px;color:var(--black)}
  .headline em{color:var(--red)}
  .lede{position:absolute;left:22px;right:22px;top:501px;font-weight:700;font-style:italic;font-stretch:88%;font-size:12px;line-height:15px;text-align:justify;color:var(--black)}
  .col{position:absolute;font-style:italic;font-size:11.5px;line-height:14.8px;text-align:justify}
  .col p{position:relative;margin-bottom:15px}
  .icon{position:absolute;width:16px;height:22px}
  .col--left{left:46px;width:136px;top:544px}
  .col--right{left:218px;width:140px;top:544px}
  .col--left .icon{left:-26px;top:8px}
  .col--right .icon{left:-26px;top:6px}
  .col-rule{position:absolute;left:199px;top:546px;width:1px;height:135px;background:var(--rule)}
  .flight-title{position:absolute;left:0;right:0;top:290px;text-align:center;font-weight:800;font-style:italic;font-size:25px;color:var(--black)}
  .flight-title em{color:var(--red)}
  .flight-title::before,.flight-title::after{content:"";position:absolute;top:17px;width:44px;height:1.5px;background:var(--red)}
  .flight-title::before{left:56px}
  .flight-title::after{right:56px}
  .features{position:absolute;list-style:none;font-style:italic;font-size:11.2px;line-height:14.5px}
  .features li{position:relative;padding-left:22px}
  .features .icon{left:0;top:0}
  .features--wide{left:22px;width:330px;top:331px}
  .features--wide li{margin-bottom:14.5px}
  .features--left{left:22px;width:180px;top:502px}
  .features--right{left:210px;width:150px;top:502px}
  .features--left li,.features--right li{margin-bottom:14px}
  .features-rule{position:absolute;left:199px;top:500px;width:1px;height:118px;background:var(--rule)}
  .booking-tab{position:absolute;left:0;top:627px;width:205px;height:17px;background:var(--red);border-radius:0 9px 9px 0;color:var(--white);font-weight:700;font-style:italic;font-size:11px;line-height:17px;padding-left:22px}
  .contacts{position:absolute;left:22px;top:650px;font-style:italic;font-size:10.5px;line-height:13.5px}
  .social{position:absolute;left:222px;top:647px;font-weight:700;font-style:italic;font-size:10.3px;line-height:13.5px;color:var(--black);padding-left:4px;border-left:1.5px solid var(--red)}
  .certificate{position:absolute;left:0;right:0;top:700px;text-align:center;font-style:italic;font-size:7px;line-height:10px;color:#444}
</style>
</head>
<body>

<section class="panel panel--front">
  <svg class="art" width="384" height="770" viewBox="0 0 384 770">
    <defs>
      <linearGradient id="burnerGlow" x1="0" y1="0" x2="0.6" y2="1">
        <stop offset="0" stop-color="#c8281c"/>
        <stop offset=".55" stop-color="#f29a3a"/>
        <stop offset="1" stop-color="#fbe3b8"/>
      </linearGradient>
      <linearGradient id="couple" x1="0" y1="0" x2="1" y2="1">
        <stop offset="0" stop-color="#a8c9d8"/>
        <stop offset=".5" stop-color="#d9b7a0"/>
        <stop offset="1" stop-color="#7fb6cf"/>
      </linearGradient>
    </defs>
    <rect width="384" height="470" fill="var(--red)"/>
    <polygon points="230,0 384,0 384,330 300,360" fill="#c70511" opacity=".5"/>
    <g role="img" aria-label="Photo: hot-air balloon envelope glowing from the burner flame">
      <polygon points="0,0 160,0 238,190 130,260 0,300" fill="url(#burnerGlow)"/>
    </g>
    <polygon points="148,0 175,0 245,175 235,190" fill="var(--black)"/>
    <g role="img" aria-label="Photo: smiling couple, woman in a straw hat riding piggyback">
      <polygon points="60,200 230,170 320,180 330,360 250,420 60,450" fill="url(#couple)"/>
    </g>
    <polygon points="0,455 384,355 384,378 0,470" fill="var(--red)"/>
    <polygon points="230,430 384,390 384,455" fill="var(--black)"/>
    <polygon points="0,470 384,378 384,400 0,480" fill="var(--white)"/>
    <polygon points="0,720 150,770 0,770" fill="var(--black)"/>
    <polygon points="140,770 384,690 384,770" fill="var(--red)"/>
    <polygon points="330,770 384,740 384,770" fill="var(--black)"/>
  </svg>

  <h1 class="title">
    <span class="title__main">KING</span>
    <span class="title__sub">VALLEY</span>
    <span class="title__tag">HOT-AIR BALLOONING</span>
  </h1>

  <h2 class="headline"><em>The perfect gourmet</em> ballooning experience</h2>
  <p class="lede">Live the romance and adventure of flying the beautiful King Valley and surrounds in a hot-air balloon at dawn</p>

  <div class="col col--left">
    <p><svg class="icon" viewBox="0 0 16 22"><ellipse cx="8" cy="7.5" rx="6.8" ry="6.8" fill="none" stroke="var(--red)" stroke-width="1.6"/><path d="M8 .8v13.4M4.5 2 5.5 13.5M11.5 2 10.5 13.5M4 14.5l2 3.5M12 14.5l-2 3.5" stroke="var(--red)" stroke-width="1.2" fill="none"/><rect x="5.5" y="18" width="5" height="3.2" fill="var(--red)"/></svg>The mountain views, once aloft, come to life in dramatic 3D with the early morning light</p>
    <p><svg class="icon" viewBox="0 0 16 22"><ellipse cx="8" cy="7.5" rx="6.8" ry="6.8" fill="none" stroke="var(--red)" stroke-width="1.6"/><path d="M8 .8v13.4M4.5 2 5.5 13.5M11.5 2 10.5 13.5M4 14.5l2 3.5M12 14.5l-2 3.5" stroke="var(--red)" stroke-width="1.2" fill="none"/><rect x="5.5" y="18" width="5" height="3.2" fill="var(--red)"/></svg>From the vineyards and patchwork of fields the views expand to the Ovens River, spectacular Mt Buffalo and the High Country beyond</p>
  </div>
  <div class="col-rule"></div>
  <div class="col col--right">
    <p><svg class="icon" viewBox="0 0 16 22"><ellipse cx="8" cy="7.5" rx="6.8" ry="6.8" fill="none" stroke="var(--red)" stroke-width="1.6"/><path d="M8 .8v13.4M4.5 2 5.5 13.5M11.5 2 10.5 13.5M4 14.5l2 3.5M12 14.5l-2 3.5" stroke="var(--red)" stroke-width="1.2" fill="none"/><rect x="5.5" y="18" width="5" height="3.2" fill="var(--red)"/></svg>Celebrate your flight with a delicious breakfast afterwards (optional)</p>
    <p><svg class="icon" viewBox="0 0 16 22"><ellipse cx="8" cy="7.5" rx="6.8" ry="6.8" fill="none" stroke="var(--red)" stroke-width="1.6"/><path d="M8 .8v13.4M4.5 2 5.5 13.5M11.5 2 10.5 13.5M4 14.5l2 3.5M12 14.5l-2 3.5" stroke="var(--red)" stroke-width="1.2" fill="none"/><rect x="5.5" y="18" width="5" height="3.2" fill="var(--red)"/></svg>Milawa is conveniently located less than an hour's drive from most places in Victoria's North East and Albury in NSW Mansfield flights are also available</p>
  </div>
</section>

<section class="panel panel--back">
  <svg class="art" width="374" height="750" viewBox="0 0 374 750">
    <defs>
      <linearGradient id="river" x1="0" y1="0" x2="1" y2="1">
        <stop offset="0" stop-color="#d9a24a"/>
        <stop offset=".45" stop-color="#8a9a6a"/>
        <stop offset="1" stop-color="#b9c7cf"/>
      </linearGradient>
      <linearGradient id="hexGlow" x1="0" y1="0" x2="0" y2="1">
        <stop offset="0" stop-color="#f3b23c"/>
        <stop offset="1" stop-color="#c8352a"/>
      </linearGradient>
      <linearGradient id="hexMist" x1="0" y1="0" x2="0" y2="1">
        <stop offset="0" stop-color="#c9d4dc"/>
        <stop offset="1" stop-color="#7f8a72"/>
      </linearGradient>
      <linearGradient id="hexSky" x1="0" y1="0" x2="0" y2="1">
        <stop offset="0" stop-color="#8fb8dc"/>
        <stop offset="1" stop-color="#d7e3ea"/>
      </linearGradient>
    </defs>
    <g role="img" aria-label="Photo: passengers in a balloon basket above a river valley at sunrise">
      <polygon points="0,0 374,0 374,140 0,275" fill="url(#river)"/>
    </g>
    <rect x="0" y="250" width="10" height="22" fill="var(--red)"/>
    <rect x="360" y="138" width="14" height="34" fill="var(--red)"/>
    <g role="img" aria-label="Photo: colourful balloon envelope lit by burner">
      <polygon points="70,190 113,215 113,265 70,290 27,265 27,215" fill="url(#hexGlow)" stroke="var(--white)" stroke-width="5"/>
    </g>
    <g role="img" aria-label="Photo: misty morning over a country town">
      <polygon points="180,160 228,188 228,243 180,271 132,243 132,188" fill="url(#hexMist)" stroke="var(--white)" stroke-width="5"/>
    </g>
    <g role="img" aria-label="Photo: striped balloon floating in clear sky">
      <polygon points="307,116 362,148 362,212 307,244 252,212 252,148" fill="url(#hexSky)" stroke="var(--white)" stroke-width="5"/>
    </g>
    <polygon points="0,726 200,750 0,750" fill="var(--red)"/>
    <polygon points="170,750 374,714 374,750" fill="var(--black)"/>
  </svg>

  <h2 class="flight-title"><em>YOUR</em> FLIGHT</h2>

  <ul class="features features--wide">
    <li><svg class="icon" viewBox="0 0 16 22"><ellipse cx="8" cy="7.5" rx="6.8" ry="6.8" fill="none" stroke="var(--red)" stroke-width="1.6"/><path d="M8 .8v13.4M4.5 2 5.5 13.5M11.5 2 10.5 13.5M4 14.5l2 3.5M12 14.5l-2 3.5" stroke="var(--red)" stroke-width="1.2" fill="none"/><rect x="5.5" y="18" width="5" height="3.2" fill="var(--red)"/></svg>One-hour sunrise balloon flight in the spectacular King Valley region in North East Victoria</li>
    <li><svg class="icon" viewBox="0 0 16 22"><ellipse cx="8" cy="7.5" rx="6.8" ry="6.8" fill="none" stroke="var(--red)" stroke-width="1.6"/><path d="M8 .8v13.4M4.5 2 5.5 13.5M11.5 2 10.5 13.5M4 14.5l2 3.5M12 14.5l-2 3.5" stroke="var(--red)" stroke-width="1.2" fill="none"/><rect x="5.5" y="18" width="5" height="3.2" fill="var(--red)"/></svg>Delicious champagne breakfast after the flight (recommended option)</li>
    <li><svg class="icon" viewBox="0 0 16 22"><ellipse cx="8" cy="7.5" rx="6.8" ry="6.8" fill="none" stroke="var(--red)" stroke-width="1.6"/><path d="M8 .8v13.4M4.5 2 5.5 13.5M11.5 2 10.5 13.5M4 14.5l2 3.5M12 14.5l-2 3.5" stroke="var(--red)" stroke-width="1.2" fill="none"/><rect x="5.5" y="18" width="5" height="3.2" fill="var(--red)"/></svg>Informative details throughout your experience with our locally based expert crew</li>
    <li><svg class="icon" viewBox="0 0 16 22"><ellipse cx="8" cy="7.5" rx="6.8" ry="6.8" fill="none" stroke="var(--red)" stroke-width="1.6"/><path d="M8 .8v13.4M4.5 2 5.5 13.5M11.5 2 10.5 13.5M4 14.5l2 3.5M12 14.5l-2 3.5" stroke="var(--red)" stroke-width="1.2" fill="none"/><rect x="5.5" y="18" width="5" height="3.2" fill="var(--red)"/></svg>The opportunity to be involved in the inflation and deflation process should you wish</li>
  </ul>

  <ul class="features features--left">
    <li><svg class="icon" viewBox="0 0 16 22"><ellipse cx="8" cy="7.5" rx="6.8" ry="6.8" fill="none" stroke="var(--red)" stroke-width="1.6"/><path d="M8 .8v13.4M4.5 2 5.5 13.5M11.5 2 10.5 13.5M4 14.5l2 3.5M12 14.5l-2 3.5" stroke="var(--red)" stroke-width="1.2" fill="none"/><rect x="5.5" y="18" width="5" height="3.2" fill="var(--red)"/></svg>Safe, friendly and professional</li>
    <li><svg class="icon" viewBox="0 0 16 22"><ellipse cx="8" cy="7.5" rx="6.8" ry="6.8" fill="none" stroke="var(--red)" stroke-width="1.6"/><path d="M8 .8v13.4M4.5 2 5.5 13.5M11.5 2 10.5 13.5M4 14.5l2 3.5M12 14.5l-2 3.5" stroke="var(--red)" stroke-width="1.2" fill="none"/><rect x="5.5" y="18" width="5" height="3.2" fill="var(--red)"/></svg>The flight lasts approximately 1 hour</li>
    <li><svg class="icon" viewBox="0 0 16 22"><ellipse cx="8" cy="7.5" rx="6.8" ry="6.8" fill="none" stroke="var(--red)" stroke-width="1.6"/><path d="M8 .8v13.4M4.5 2 5.5 13.5M11.5 2 10.5 13.5M4 14.5l2 3.5M12 14.5l-2 3.5" stroke="var(--red)" stroke-width="1.2" fill="none"/><rect x="5.5" y="18" width="5" height="3.2" fill="var(--red)"/></svg>The entire experience takes about 3-4 hours</li>
  </ul>
  <div class="features-rule"></div>
  <ul class="features features--right">
    <li><svg class="icon" viewBox="0 0 16 22"><ellipse cx="8" cy="7.5" rx="6.8" ry="6.8" fill="none" stroke="var(--red)" stroke-width="1.6"/><path d="M8 .8v13.4M4.5 2 5.5 13.5M11.5 2 10.5 13.5M4 14.5l2 3.5M12 14.5l-2 3.5" stroke="var(--red)" stroke-width="1.2" fill="none"/><rect x="5.5" y="18" width="5" height="3.2" fill="var(--red)"/></svg>Suitable from age 7 to 97</li>
    <li><svg class="icon" viewBox="0 0 16 22"><ellipse cx="8" cy="7.5" rx="6.8" ry="6.8" fill="none" stroke="var(--red)" stroke-width="1.6"/><path d="M8 .8v13.4M4.5 2 5.5 13.5M11.5 2 10.5 13.5M4 14.5l2 3.5M12 14.5l-2 3.5" stroke="var(--red)" stroke-width="1.2" fill="none"/><rect x="5.5" y="18" width="5" height="3.2" fill="var(--red)"/></svg>Gift Vouchers are also available</li>
    <li><svg class="icon" viewBox="0 0 16 22"><ellipse cx="8" cy="7.5" rx="6.8" ry="6.8" fill="none" stroke="var(--red)" stroke-width="1.6"/><path d="M8 .8v13.4M4.5 2 5.5 13.5M11.5 2 10.5 13.5M4 14.5l2 3.5M12 14.5l-2 3.5" stroke="var(--red)" stroke-width="1.2" fill="none"/><rect x="5.5" y="18" width="5" height="3.2" fill="var(--red)"/></svg>Contact us for exclusive flight options at your custom location</li>
  </ul>

  <div class="booking-tab">For bookings or more information:</div>
  <p class="contacts">www.skylarkaerialtours.com.au<br>flights@skylarkaerialtours.com.au<br>or call our friendly team on 1300 555 014</p>
  <p class="social">Find us also on Facefeed,<br>Snapgram and TravelRater<br>@skylarkaerialtoursaus</p>

  <p class="certificate">Skylark Aerial Tours operates under Air Operator's Certificate CS40118-02<br>issued by the National Aviation Safety Regulator</p>
</section>

</body>
</html>
```